Cleaning Company Banner

Looking to have a Banner made that shows our contact information and shows what we do with good imagery to catch cars driving by. Will be a 6' x 3' banner (landscape). Attached our logo and flyer that we currently hand out.

```html
<!DOCTYPE html>
<html lang="en">
<head>
<meta charset="utf-8">
<title>BrightPath Cleaning – Banner</title>
<link href="https://fonts.googleapis.com/css2?family=Montserrat:wght@400;600;700;800&display=swap" rel="stylesheet">
<style>
  :root {
    --page-bg: #eef0f2;
    --banner-white: #ffffff;
    --corner-blue: #2f86c9;
    --brand-teal: #2aa79b;
    --navy: #1b2350;
    --dot-blue: #6aaddf;
    --dot-blue-deep: #5fa3d8;
    --dot-mint: #8fd6cf;
    --dot-teal: #2fb9a6;
    --photo-light: #e6eae4;
    --photo-tone: #c9e6a0;
  }
  html, body {
    margin: 0;
    padding: 0;
    width: 1200px;
    height: 800px;
    overflow: hidden;
    background: var(--page-bg);
  }
  .banner {
    position: absolute;
    left: 40px;
    top: 98px;
    width: 1120px;
    height: 604px;
    background: var(--banner-white);
    overflow: hidden;
    font-family: "Montserrat", sans-serif;
    box-shadow: 0 6px 24px rgba(0,0,0,0.08);
  }
  .backdrop {
    position: absolute;
    inset: 0;
  }
  .cleaning-photo {
    position: absolute;
    left: 760px;
    top: 0;
    width: 360px;
    height: 443px;
    background: linear-gradient(160deg, var(--photo-light) 0%, var(--photo-tone) 100%);
  }
  .brand {
    position: absolute;
    left: 40px;
    top: 214px;
    width: 270px;
    display: flex;
    align-items: center;
    justify-content: center;
    gap: 12px;
  }
  .brand-dot {
    width: 22px;
    height: 22px;
    border-radius: 50%;
    background: var(--brand-teal);
    flex: none;
  }
  .brand-name {
    margin: 0;
    color: var(--brand-teal);
    font-weight: 700;
    font-size: 30px;
    line-height: 1.05;
    letter-spacing: 1px;
    text-transform: uppercase;
  }
  .tagline {
    position: absolute;
    left: 22px;
    top: 312px;
    width: 300px;
    margin: 0;
    text-align: center;
    color: var(--navy);
    font-weight: 400;
    font-size: 29px;
    line-height: 40px;
  }
  .contact {
    position: absolute;
    left: 26px;
    top: 494px;
    margin: 0;
    color: var(--navy);
  }
  .contact-phone {
    display: block;
    font-weight: 700;
    font-size: 40px;
    line-height: 46px;
    letter-spacing: 0.5px;
  }
  .contact-email {
    display: block;
    font-weight: 600;
    font-size: 26px;
    line-height: 36px;
  }
  .headline {
    position: absolute;
    right: 42px;
    top: 472px;
    margin: 0;
    text-align: right;
    color: var(--navy);
    font-weight: 800;
    font-size: 40px;
    line-height: 50px;
    text-transform: uppercase;
    letter-spacing: 0.5px;
  }
</style>
</head>
<body>
  <main class="banner">
    <svg class="backdrop" width="1120" height="604" viewBox="0 0 1120 604" aria-hidden="true">
      <defs>
        <radialGradient id="marble-fill" cx="0.55" cy="0.4" r="0.7">
          <stop offset="0" stop-color="#f4f5f6"/>
          <stop offset="1" stop-color="#e3e6e8"/>
        </radialGradient>
      </defs>
      <circle class="marble-disc" cx="742" cy="249" r="424" fill="url(#marble-fill)"/>
      <path class="corner-accent" d="M0 0 H150 C110 60 70 140 0 212 Z" fill="var(--corner-blue)"/>
      <circle class="dot" cx="404" cy="207" r="37" fill="var(--dot-blue)"/>
      <circle class="dot" cx="598" cy="129" r="33" fill="var(--dot-mint)"/>
      <circle class="dot" cx="629" cy="310" r="31" fill="var(--dot-teal)"/>
      <circle class="dot" cx="461" cy="505" r="54" fill="var(--dot-blue-deep)"/>
    </svg>

    <div class="cleaning-photo" role="img" aria-label="Photo of a gloved hand wiping a surface with a microfibre cloth"></div>

    <div class="brand">
      <span class="brand-dot"></span>
      <p class="brand-name">BrightPath<br>Cleaning</p>
    </div>

    <p class="tagline">Quality driven and reliable to take care of all your cleaning needs!</p>

    <p class="contact">
      <span class="contact-phone">(555) 214 - 7390</span>
      <span class="contact-email">hello@brightpathclean.com</span>
    </p>

    <h1 class="headline">Cleaning solution<br>for all!</h1>
  </main>
</body>
</html>
```